Law Firm Web Design Project

I need a website design for my law firm. I have attached to this description the URL of a website I liked with a description of the elements of that website that appeal to me.

I am also attaching my law firm's logo, so you can review that design when you create the website design.

Reference Site: www.harbormeadowfamilycounsel.com

What we like about this site:
• The different layers
• Subtle designs, textures, curves
• 3 dimensional
• Floating effect
• Simple logo that stands out (we are providing logo)
• Prominent phone number
• Location of Areas of Practice
oDivorce, Legal Separation, Paternity, Spousal Maintenance, Child Custody, Child Support, Protective Orders, Community Property, Business Evaluations
• The limited amount of links across the top
o Home, Meet Our Attorney, FAQ, Contact Us
• Request A Consultation click through
• Right side bar with the moving icons
• Badges

Other Tips:
• We don’t want the website to be dark. The logo can standout and the website can have its own colors and flow.
• We would like there to be a “call to action” or way to get in touch on every page and every page view
• We would like a place for credit card icons at the bottom of the page
• Strong, yet elegant
• Finally, just use the website provided as a guide. Explore different colors, textures, shapes, shadows etc.
Updates

I would prefer the website have colors that are complementary to my logo and that are strong and elegant.  I like black, gold, amber, and tan colors.  Black should be used sparingly as an accent only, since I don't want the website to be too dark.

Please review the website I provided as an example in my project description.  I really like the three dimensional aspects of that website (web page floating on top of a background and the logo in the upper left floating on top of the web page).  I also like the use of "swirling" on the background and the webpage.  I hope this additional information is helpful.

Requirements
Must have
• I need a place to insert "client testimonials", a place to insert four logos of awards the law firm has received, a place for people to fill out a form to contact the law firm via email, and a place for people to click to review articles I have written.

```html
<!DOCTYPE html>
<html lang="en">
<head>
<meta charset="utf-8">
<title>Ashcombe Law</title>
<link rel="stylesheet" href="https://fonts.googleapis.com/css2?family=Libre+Baskerville:wght@400;700&family=Didact+Gothic&display=swap">
<style>
:root{
  --olive:#857234;
  --olive-dark:#6e5d27;
  --gold:#e2c77f;
  --gold-light:#ecd89f;
  --gold-deep:#c9a94f;
  --sand:#cdb87c;
  --amber:#b08a2a;
  --ink:#1b1b1b;
  --text:#3a2f14;
  --white:#ffffff;
  --accent:#c98a1a;
}
*{box-sizing:border-box;margin:0;padding:0}
html,body{width:777px;height:1200px;overflow:hidden}
body{position:relative;background:var(--olive);font-family:"Didact Gothic",sans-serif;color:var(--text)}
.abs{position:absolute}
.serif{font-family:"Libre Baskerville",serif}

.page{left:32px;top:0;width:712px;height:1082px;background:linear-gradient(180deg,var(--gold-light) 0,var(--gold) 40%,#dcbf72 100%);box-shadow:0 0 12px rgba(0,0,0,.35)}
.footer-band{left:0;top:1082px;width:777px;height:118px;background:var(--sand)}

.logo-tab{left:19px;top:0;width:282px;height:129px;z-index:3;filter:drop-shadow(0 3px 4px rgba(0,0,0,.3))}
.brand{left:104px;top:38px;font-size:27px;color:var(--amber);letter-spacing:.5px;z-index:4}
.brand-sub{left:150px;top:71px;font-size:11px;color:var(--amber);letter-spacing:2px;z-index:4}
.brand-mark{left:44px;top:46px;width:36px;height:36px;background:var(--gold-deep);z-index:4}

.phone-top{right:43px;top:18px;font-size:18px;color:var(--ink)}
.phone-top small{font-size:13px}

.nav{left:297px;top:54px;width:447px;height:37px;background:linear-gradient(180deg,#3a3a3a,#0d0d0d);display:flex;justify-content:space-around;align-items:center;padding-left:40px}
.nav a{color:var(--white);font-size:12.5px;text-decoration:none}

.hero{left:32px;top:91px;width:712px;height:266px;background:radial-gradient(ellipse at 70% 45%,#e9c8a5 0,#c9a77a 35%,#9c8d5f 70%,#7e7a4c 100%)}
.hero-line{font-size:27px;color:var(--ink)}
.cta{left:19px;top:276px;width:261px;height:45px;background:linear-gradient(180deg,#3b3b3b,#0b0b0b);color:var(--white);font-size:18px;display:flex;align-items:center;padding-left:34px;box-shadow:0 3px 6px rgba(0,0,0,.4)}

.practice{left:32px;top:377px;width:174px;height:304px;background:linear-gradient(180deg,#d8b866,#c9a74f);border-radius:0 0 10px 0;box-shadow:2px 3px 6px rgba(0,0,0,.25)}
.practice h2{height:38px;background:linear-gradient(180deg,#3a3a3a,#0d0d0d);color:var(--white);font-size:13.5px;font-weight:400;padding:9px 0 0 22px}
.practice ul{list-style:none;padding:13px 10px 0 14px}
.practice li{font-size:11px;color:var(--white);height:24.5px;line-height:22px;border-bottom:1px solid rgba(255,255,255,.35);padding-left:9px}

.badge{background:var(--white)}

.intro-title{left:224px;top:384px;width:320px;font-size:13px;font-weight:700;color:var(--ink)}
.intro-body{left:224px;top:426px;width:320px;font-size:10.5px;line-height:13px;text-indent:30px;text-align:justify}
.more{font-size:9.5px;color:var(--ink);text-decoration:underline}
.rule{left:222px;top:546px;width:324px;height:3px;background:var(--amber);border-radius:2px}
.section-title{font-size:17px;color:var(--ink)}

.thumb{width:150px;height:75px;border:4px solid var(--white);box-shadow:1px 2px 4px rgba(0,0,0,.35)}
.art-title{font-size:10px;font-weight:700;color:var(--ink)}
.art-date{font-size:9px;color:var(--accent)}
.art-body{width:152px;font-size:10px;line-height:12.5px}

.testimonial{left:225px;top:843px;width:317px;height:169px;background:linear-gradient(180deg,#fbfaf5,#ecebe4);box-shadow:0 6px 10px rgba(0,0,0,.35);padding:12px 16px}
.testimonial h3{font-size:17px;font-weight:400;color:var(--ink);margin-bottom:8px}
.testimonial p{font-size:10px;line-height:13px;font-style:italic;color:var(--ink)}
.testimonial .by{text-align:right;font-style:normal;font-weight:700;margin-top:8px}
.testimonial .all{text-align:right;font-style:normal;margin-top:12px;font-size:9.5px;text-decoration:underline}

.side-btn{left:558px;width:176px;height:46px;border-radius:5px;display:flex;align-items:center;gap:10px;padding-left:8px;font-size:15px;white-space:nowrap}
.side-btn.dark{background:linear-gradient(180deg,#3e3e3e,#0b0b0b);color:var(--white);font-size:16.5px}
.side-btn.gold{background:linear-gradient(180deg,#d9bd6c,#b8963c);color:#4a3a10;box-shadow:inset 0 1px 0 rgba(255,255,255,.4),0 2px 3px rgba(0,0,0,.2)}
.icon{width:34px;height:34px;flex:none}

.qc-title{right:43px;top:635px;font-size:14px;color:var(--ink)}
.field{left:558px;width:176px;background:var(--white);border-radius:3px;font-size:9px;color:#333;padding:3px 5px}
.send{left:681px;top:829px;width:52px;height:18px;border-radius:3px;background:linear-gradient(180deg,#f3f3f3,#cfcfcf);font-size:10px;font-weight:700;text-align:center;line-height:18px;color:var(--ink)}

.cards{left:581px;top:1048px;display:flex;gap:3px}
.card{width:36px;height:23px;background:var(--white);border:1px solid #b89c52;font-size:9px;display:flex;align-items:center;justify-content:center;color:var(--ink)}

.foot-links{left:14px;top:1097px;font-size:10px;color:var(--ink)}
.foot-links span{margin:0 6px}
.copy{left:14px;top:1114px;font-size:9px;font-weight:700;color:var(--ink)}
.address{right:43px;top:1097px;font-size:9.5px;color:var(--ink);text-align:right;line-height:16px}
.social{right:33px;top:1134px;display:flex;gap:4px}
.social span{font-size:9px;color:var(--white);background:#4f6f8f;padding:3px 4px;border-radius:2px}
</style>
</head>
<body>
<div class="abs page"></div>
<div class="abs footer-band"></div>

<div class="abs hero" role="img" aria-label="Photo of a smiling mother hugging her young son outdoors"></div>

<svg class="abs logo-tab" viewBox="0 0 282 129">
  <path d="M0 0 H282 V20 C282 50 270 115 240 118 L12 126 Z" fill="#c9a94f"/>
  <path d="M0 0 H276 V18 C276 46 266 106 236 110 L8 118 L0 118 Z" fill="#ffffff"/>
</svg>
<div class="abs brand-mark"></div>
<div class="abs brand serif">Ashcombe</div>
<div class="abs brand-sub serif">LAW</div>

<div class="abs phone-top serif"><small>Call Us</small> (555) 238.4410</div>

<nav class="abs nav">
  <a href="#">Home</a><a href="#">Meet Our Attorney</a><a href="#">FAQ</a><a href="#">Contact Us</a>
</nav>

<div class="abs hero-line serif" style="left:66px;top:180px">Let us solve</div>
<div class="abs hero-line serif" style="left:133px;top:208px">your problem</div>
<div class="abs cta">Request a Consultation</div>

<aside class="abs practice">
  <h2 class="serif">Areas Of Practice</h2>
  <ul>
    <li>Divorce</li><li>Legal Separation</li><li>Paternity</li><li>Spousal Maintenance</li><li>Child Custody</li><li>Child Support</li><li>Protective Orders</li><li>Community Property</li><li>Business Evaluations</li>
  </ul>
</aside>

<div class="abs badge" style="left:95px;top:736px;width:54px;height:89px;border-radius:4px;background:#2f6f8f"></div>
<div class="abs badge" style="left:59px;top:858px;width:122px;height:50px;background:#d8c3b0;border-radius:3px"></div>
<div class="abs badge" style="left:66px;top:940px;width:114px;height:75px"></div>

<h1 class="abs intro-title serif">Ashcombe Law provide nationwide legal services.</h1>
<p class="abs intro-body">Lorem ipsum dolor sit amet, consectetur adipisicing elit, sed do eiusmod tempor incididunt ut labore et dolore magna aliqua. Ut enim ad minim veniam, quis nostrud exercitation ullamco laboris nisi ut aliquip ex ea commodo consequat. Duis aute irure dolor in reprehenderit in voluptate velit esse cillum dolore eu fugiat nulla pariatur. Excepteur sint occaecat cupidatat non proident, sunt in culpa qui officia deserunt mollit anim id est</p>
<div class="abs more" style="left:436px;top:525px">Learn More About Us ▸</div>
<div class="abs rule"></div>

<h2 class="abs section-title serif" style="left:224px;top:562px">Articles</h2>
<div class="abs thumb" style="left:225px;top:594px;background:linear-gradient(135deg,#f0b050,#a5561b 60%,#5a2a0e)" role="img" aria-label="Photo of a judge's gavel and scales"></div>
<div class="abs thumb" style="left:391px;top:594px;background:linear-gradient(90deg,#5c3a18,#9a7a3a,#4a2e14,#8c6a2e)" role="img" aria-label="Photo of law books on a shelf"></div>

<div class="abs art-title" style="left:224px;top:678px">Lorem ipsum dolor sit amet</div>
<div class="abs art-date" style="left:224px;top:689px">March 16, 2012</div>
<p class="abs art-body" style="left:224px;top:709px">Consectetur adipisicing elit, sed do eiusmod tempor incididunt ut labore et dolore magna aliqua. Ut enim ad minim veniam, quis nostrud exercitation ullamco laboris nisi ut aliquip ex ea commodo consequat.</p>
<div class="abs more" style="left:332px;top:787px">Read More</div>

<div class="abs art-title" style="left:391px;top:678px">Lorem ipsum dolor sit amet</div>
<div class="abs art-date" style="left:391px;top:689px">March 16, 2012</div>
<p class="abs art-body" style="left:391px;top:709px">Consectetur adipisicing elit, sed do eiusmod tempor incididunt ut labore et dolore magna aliqua. Ut enim ad minim veniam, quis nostrud exercitation ullamco laboris nisi ut aliquip ex ea commodo consequat.</p>
<div class="abs more" style="left:498px;top:787px">Read More</div>

<section class="abs testimonial">
  <h3 class="serif">Client Testimonial</h3>
  <p>“Lorem ipsum dolor sit amet, consectetur adipisicing elit, sed do eiusmod tempor incididunt ut labore et dolore magna aliqua. Ut enim ad minim veniam, quis nostrud exercitation ullamco laboris nisi ut aliquip ex ea commodo consequat. Duis aute irure dolor in reprehenderit in voluptate velit esse cillum dolore eu fugiat nulla pariatur.”</p>
  <p class="by">-John Doe</p>
  <p class="all">Read All Testimonials ▸</p>
</section>

<div class="abs side-btn dark serif" style="top:377px">
  <svg class="icon" viewBox="0 0 34 34"><circle cx="17" cy="17" r="16" fill="#555"/><path d="M12 9 l4 4 -2 3 c1 2 3 4 5 5 l3 -2 4 4 -3 3 c-7 -1 -13 -7 -14 -14 Z" fill="#fff"/></svg>Click to Call</div>
<div class="abs side-btn gold serif" style="top:437px">
  <svg class="icon" viewBox="0 0 34 34"><path d="M12 20 l-3 11 5 -3 3 4 2 -10 Z M22 20 l3 11 -5 -3 -3 4 -2 -10 Z" fill="#2a2410"/><circle cx="17" cy="13" r="9" fill="#2a2410"/></svg>Awards</div>
<div class="abs side-btn gold serif" style="top:496px">
  <svg class="icon" viewBox="0 0 34 34"><ellipse cx="17" cy="15" rx="14" ry="10" fill="#2a2410"/><path d="M9 22 l-3 8 9 -6 Z" fill="#2a2410"/></svg>Testimonials</div>
<div class="abs side-btn gold serif" style="top:556px">
  <svg class="icon" viewBox="0 0 34 34"><circle cx="14" cy="14" r="10" fill="none" stroke="#2a2410" stroke-width="4"/><path d="M21 21 l9 9" stroke="#2a2410" stroke-width="5" stroke-linecap="round"/></svg>Case Evaluation</div>

<div class="abs qc-title serif">Quick Contact</div>
<div class="abs field" style="top:661px;height:19px">Name:</div>
<div class="abs field" style="top:684px;height:18px">Email:</div>
<div class="abs field" style="top:707px;height:18px">Phone:</div>
<div class="abs field" style="top:730px;height:90px">Message:</div>
<div class="abs send">Send</div>

<div class="abs cards">
  <div class="card">Ambera</div><div class="card">Valto</div><div class="card">Merix</div><div class="card">Dovera</div>
</div>

<div class="abs foot-links">Home<span>|</span>Meet Our Attorney<span>|</span>FAQ<span>|</span>Contact Us</div>
<div class="abs copy">© 2012 Ashcombe Law</div>
<div class="abs address">123 Your Address 123456 CITY-COUNTRY<br>Tel : 01 23 45 67 89 &nbsp;&nbsp; Fax : 01 23 45 67 89</div>
<div class="abs social"><span>Proflink</span><span>Chatter</span><span>Circlebook</span></div>
</body>
</html>
```